Chill Bo
frozen yogurt and more
Corporate
Tara Kessler
Owner
4182 Larkspur Ln.
Columbus IN. 47358
tarasglow@quillpost.com
Don't have store open yet so have no address or phone numbers. We want logo font the same but would like a standard clean font for the rest of the info

```html
<!DOCTYPE html>
<html lang="en">
<head>
<meta charset="utf-8">
<title>Chill Bo – Business Cards</title>
<link rel="stylesheet" href="https://fonts.googleapis.com/css2?family=Open+Sans:wght@400;600;700&display=swap">
<style>
  :root {
    --bg: #efe9df;
    --card: #ffffff;
    --brown: #5a3a22;
    --brown-text: #4a2f1d;
    --green: #7cb342;
    --body: #3b2a1e;
    --divider: #cfc6bc;
  }
  * { margin: 0; padding: 0; box-sizing: border-box; }
  html, body { width: 1200px; height: 852px; overflow: hidden; }
  body {
    background: var(--bg);
    font-family: "Open Sans", Arial, sans-serif;
    position: relative;
  }
  .card {
    position: absolute;
    width: 560px;
    height: 320px;
    background: var(--card);
    border-radius: 14px;
    overflow: hidden;
    box-shadow: 0 6px 18px rgba(60, 40, 20, 0.18);
  }
  .card-front { left: 70px; top: 90px; }
  .card-back { left: 570px; top: 440px; }
  .card-corners { position: absolute; inset: 0; width: 100%; height: 100%; }

  .brand { display: flex; align-items: center; gap: 10px; }
  .brand-dot { width: 18px; height: 18px; border-radius: 50%; background: var(--green); }
  .brand-name { font-weight: 600; font-size: 40px; color: var(--brown-text); line-height: 1; }
  .brand-tagline {
    font-size: 13px; letter-spacing: 3px; color: var(--green);
    font-weight: 600; text-transform: uppercase; margin-top: 6px;
  }

  /* Front card */
  .front-content {
    position: absolute; inset: 0;
    display: flex; flex-direction: column; align-items: center;
    padding-top: 66px; text-align: center; color: var(--body);
  }
  .front-content .brand-tagline { margin-bottom: 28px; }
  .person { font-size: 16px; font-weight: 700; color: var(--brown-text); }
  .person .role { color: var(--green); font-weight: 600; }
  .contact-line { font-size: 12px; margin-top: 8px; }
  .contact-line.address { margin-top: 10px; }

  /* Back card */
  .back-logo {
    position: absolute; left: 0; top: 0; width: 290px; height: 100%;
    display: flex; flex-direction: column; align-items: center; justify-content: center;
  }
  .back-divider {
    position: absolute; left: 292px; top: 50px; width: 1px; height: 190px;
    background: var(--divider);
  }
  .back-info {
    position: absolute; left: 314px; top: 48px; color: var(--body); font-size: 12px;
  }
  .back-info .name { font-size: 16px; font-weight: 700; color: var(--brown-text); }
  .back-info .role { color: var(--green); font-weight: 600; font-size: 13px; margin-top: 2px; }
  .back-info .address { margin-top: 26px; line-height: 1.5; }
  .back-info .links { margin-top: 20px; }
  .back-info .link-row { display: flex; align-items: center; gap: 7px; margin-top: 4px; }
  .back-info .icon { width: 11px; height: 11px; flex: none; }
</style>
</head>
<body>

  <section class="card card-front">
    <svg class="card-corners" viewBox="0 0 560 320" aria-hidden="true">
      <path d="M400 0 Q510 18 560 110 L560 0 Z" fill="var(--brown)"/>
      <path d="M388 0 Q505 22 560 125" fill="none" stroke="var(--green)" stroke-width="4"/>
      <path d="M0 210 Q40 300 160 320 L0 320 Z" fill="var(--brown)"/>
      <path d="M0 195 Q38 305 175 320" fill="none" stroke="var(--green)" stroke-width="4"/>
    </svg>
    <div class="front-content">
      <div class="brand">
        <span class="brand-dot"></span>
        <span class="brand-name">Chill Bo</span>
      </div>
      <div class="brand-tagline">Frozen Yogurt</div>
      <div class="person">Tara Kessler / <span class="role">Owner</span></div>
      <div class="contact-line">tarasglow@quillpost.com</div>
      <div class="contact-line address">4182 Larkspur Ln. Columbus IN. 47358</div>
    </div>
  </section>

  <section class="card card-back">
    <svg class="card-corners" viewBox="0 0 560 320" aria-hidden="true">
      <path d="M440 0 Q525 12 560 70 L560 0 Z" fill="var(--brown)"/>
      <path d="M425 0 Q520 16 560 85" fill="none" stroke="var(--green)" stroke-width="4"/>
      <path d="M0 175 Q60 300 250 320 L0 320 Z" fill="var(--brown)"/>
      <path d="M0 160 Q55 305 270 320" fill="none" stroke="var(--green)" stroke-width="4"/>
    </svg>
    <div class="back-logo">
      <div class="brand">
        <span class="brand-dot"></span>
        <span class="brand-name">Chill Bo</span>
      </div>
      <div class="brand-tagline">Frozen Yogurt</div>
    </div>
    <div class="back-divider"></div>
    <div class="back-info">
      <div class="name">Tara Kessler</div>
      <div class="role">Owner</div>
      <div class="address">4182 Larkspur Ln.<br>Columbus IN. 47358</div>
      <div class="links">
        <div class="link-row">
          <svg class="icon" viewBox="0 0 12 12" aria-hidden="true">
            <rect x="1" y="2.5" width="10" height="7" rx="1" fill="var(--brown)"/>
            <path d="M1.5 3 L6 6.5 L10.5 3" fill="none" stroke="#fff" stroke-width="1"/>
          </svg>
          <span>tarasglow@quillpost.com</span>
        </div>
      </div>
    </div>
  </section>

</body>
</html>
```